Bluestone Advisory & Mgmt - Professional Business Cards

Hi!

I am a Real Estate Developer and Construction Consultant.

I have a lot of inspiration from previous designs and would be open to using the attached Designs as a starting point. I would like to see these styles incorporated into your designs.

I really need professional business card to go with it that includes my important info.

Look forward to seeing your designs!.

Target Market(s)

My Target market are building owners, lawyers, consultants.

Industry/Entity Type

Real Estate Development

Contact Information for Business Card

My Name: Dorian Pelkey
My Title: Principle
Company Name: Bluestone Advisory & Mgmt, LLC
Address: 348 West 71st Street, 9th FL New York, NY 10010
Mobile: 917.806.3971
Website: bam-hvx.example

Font styles to use
Serif
Sans Serif

Colors

Designer to choose colors to be used in the design.

Requirements
Must have
• Must incorporate the logo attached or have new that looks similar.
• Must use professional font that will be seen and judged by wealthy land owners and developers.
• Must incorporate some of the color green.
Should not have
• Photo's or pictures of people or buildings of any kind.

```html
<!DOCTYPE html>
<html lang="en">
<head>
<meta charset="utf-8">
<title>Bluestone Advisory &amp; Mgmt – Business Cards</title>
<link rel="stylesheet" href="https://fonts.googleapis.com/css2?family=Oswald:wght@500&family=Montserrat:wght@400&family=Raleway:wght@400&display=swap">
<style>
  :root {
    --backdrop: #161616;
    --card: #1d1d1d;
    --card-edge: #262626;
    --foil: #bdbdbd;
    --foil-soft: #9c9c9c;
    --accent: #4caf6e;
  }
  * { margin: 0; padding: 0; box-sizing: border-box; }
  html, body { width: 1200px; height: 900px; overflow: hidden; }
  body {
    background: var(--backdrop);
    position: relative;
    font-family: "Montserrat", sans-serif;
  }
  .card {
    position: absolute;
    left: 320px;
    width: 560px;
    height: 320px;
    background: var(--card);
    border: 1px solid var(--card-edge);
    box-shadow: 0 10px 30px rgba(0,0,0,0.6);
  }
  .card--front { top: 100px; }
  .card--back { top: 470px; }

  .brand {
    position: absolute;
    inset: 0;
    display: flex;
    align-items: center;
    justify-content: center;
    gap: 16px;
  }
  .brand__mark {
    width: 46px;
    height: 46px;
    background: var(--accent);
    flex: none;
  }
  .brand__name {
    font-family: "Raleway", sans-serif;
    font-weight: 400;
    font-size: 28px;
    letter-spacing: 1px;
    color: var(--foil);
    white-space: nowrap;
  }

  .holder {
    position: absolute;
    top: 108px;
    right: 290px;
    text-align: right;
  }
  .holder__name {
    font-family: "Oswald", sans-serif;
    font-weight: 500;
    font-size: 36px;
    letter-spacing: 1px;
    text-transform: uppercase;
    color: var(--foil);
    line-height: 1.1;
    white-space: nowrap;
  }
  .holder__title {
    font-size: 15px;
    letter-spacing: 1px;
    color: var(--accent);
    margin-top: 2px;
  }
  .divider {
    position: absolute;
    left: 300px;
    top: 112px;
    width: 1px;
    height: 70px;
    background: var(--accent);
  }
  .contact {
    position: absolute;
    left: 322px;
    top: 110px;
    list-style: none;
  }
  .contact__item {
    display: flex;
    align-items: center;
    gap: 10px;
    font-size: 15px;
    letter-spacing: 0.5px;
    color: var(--foil);
    line-height: 24px;
    white-space: nowrap;
  }
  .contact__icon { width: 12px; height: 12px; flex: none; }
  .address {
    position: absolute;
    left: 34px;
    bottom: 34px;
    font-size: 14px;
    letter-spacing: 0.5px;
    color: var(--foil-soft);
    white-space: nowrap;
  }
</style>
</head>
<body>
  <section class="card card--front" aria-label="Card front">
    <div class="brand">
      <span class="brand__mark" aria-hidden="true"></span>
      <span class="brand__name">Bluestone Advisory Management</span>
    </div>
  </section>

  <section class="card card--back" aria-label="Card back">
    <div class="holder">
      <p class="holder__name">Dorian Pelkey</p>
      <p class="holder__title">Principle</p>
    </div>
    <div class="divider"></div>
    <ul class="contact">
      <li class="contact__item">
        <svg class="contact__icon" viewBox="0 0 12 12" aria-hidden="true"><path d="M2.5 1 L4.5 1 L5 3.5 L3.8 4.5 Q5 7 7.5 8.2 L8.5 7 L11 7.5 L11 9.5 Q10 11 8 10.7 Q2 9 1.2 3 Q1 1.5 2.5 1 Z" fill="#4caf6e"/></svg>
        917.806.3971
      </li>
      <li class="contact__item">
        <svg class="contact__icon" viewBox="0 0 12 12" aria-hidden="true"><rect x="1" y="2.5" width="10" height="7" fill="none" stroke="#4caf6e" stroke-width="1.2"/><path d="M1 2.5 L6 6.5 L11 2.5" fill="none" stroke="#4caf6e" stroke-width="1.2"/></svg>
        info@bam-hvx.example
      </li>
      <li class="contact__item">
        <svg class="contact__icon" viewBox="0 0 12 12" aria-hidden="true"><circle cx="6" cy="6" r="5" fill="none" stroke="#4caf6e" stroke-width="1.1"/><ellipse cx="6" cy="6" rx="2.2" ry="5" fill="none" stroke="#4caf6e" stroke-width="1"/><path d="M1 6 H11" stroke="#4caf6e" stroke-width="1"/></svg>
        www.bam-hvx.example
      </li>
    </ul>
    <p class="address">348 West 71st Street, 9th FL New York, NY 10010</p>
  </section>
</body>
</html>
```